Mobile technology Business Card Design Project

We need a business card design for our company based in Sydeny Australia, that takes a company's desktop sites and creates a mobile site compatible to all mobile/smartphone devices. This allows greater ease of use and generally faster business conversion than customers using a desktop site.
Our company is called Zelvora but we refer to it as Zelvora Solutions. If this could be represented somewhere on the business card that would be great.
Am open to suggestions regarding the colours but a high tech  theme would be good.
Happy bidding!

Target Market(s)
Business owner that has a website and is reasonably savvy regarding online/mobile marketing.
Industry/Entity Type
Business
Requirements
Must have
- Business card details:
Director Peter Hawkley
Address: 4/15 Brenton rd, Kelmore. 2047
Email: tbc
Web: www.zelvora-example.com.au
The cards need to have two different names for the two directors.
Damien Ferrowe & Peter Hawkley (two separate business cards)

```html
<!DOCTYPE html>
<html lang="en">
<head>
<meta charset="utf-8">
<title>Zelvora Business Card</title>
<link rel="stylesheet" href="https://fonts.googleapis.com/css2?family=Questrial&family=Montserrat:wght@600;700&display=swap">
<style>
  :root {
    --backdrop: #7a5a3c;
    --card-blue: #19a4dd;
    --card-blue-light: #3cb6e8;
    --card-blue-deep: #1290c8;
    --ink-dark: #16222e;
    --ink-white: #ffffff;
  }
  * { box-sizing: border-box; margin: 0; padding: 0; }
  html, body {
    width: 1200px;
    height: 900px;
    overflow: hidden;
    background: var(--backdrop);
  }
  .card {
    position: absolute;
    left: 100px;
    top: 170px;
    width: 1000px;
    height: 560px;
    background: radial-gradient(circle at 31% 38%, var(--card-blue-light) 0%, var(--card-blue) 45%, var(--card-blue-deep) 100%);
    font-family: "Questrial", sans-serif;
    color: var(--ink-dark);
  }
  .brand-mark {
    position: absolute;
    left: 225px;
    top: 110px;
    width: 180px;
    height: 180px;
    border-radius: 50%;
    background: var(--ink-white);
  }
  .brand-name {
    position: absolute;
    left: 115px;
    top: 330px;
    width: 400px;
    text-align: center;
    font-size: 46px;
    line-height: 1;
    color: var(--ink-white);
    letter-spacing: 1px;
  }
  .tagline {
    position: absolute;
    left: 115px;
    top: 400px;
    width: 400px;
    text-align: center;
    font-size: 20px;
    letter-spacing: 1px;
    color: var(--ink-dark);
  }
  .contact-list {
    position: absolute;
    left: 550px;
    top: 116px;
    list-style: none;
  }
  .contact-item {
    display: flex;
    align-items: center;
    height: 44px;
    font-size: 21px;
    color: var(--ink-dark);
  }
  .contact-icon {
    width: 26px;
    height: 26px;
    margin-right: 18px;
    flex: none;
  }
  .contact-icon * {
    fill: none;
    stroke: var(--ink-white);
    stroke-width: 1.8;
    stroke-linecap: round;
    stroke-linejoin: round;
  }
  .divider {
    position: absolute;
    left: 550px;
    top: 303px;
    width: 300px;
    height: 2px;
    background: var(--ink-white);
  }
  .person-name {
    position: absolute;
    left: 590px;
    top: 328px;
    font-family: "Montserrat", sans-serif;
    font-weight: 700;
    font-size: 27px;
    color: var(--ink-white);
  }
  .person-role {
    position: absolute;
    left: 590px;
    top: 364px;
    font-family: "Montserrat", sans-serif;
    font-weight: 600;
    font-size: 20px;
    color: var(--ink-dark);
  }
</style>
</head>
<body>
  <div class="card">
    <div class="brand-mark"></div>
    <div class="brand-name">Zelvora</div>
    <div class="tagline">Taking Your Site Mobile</div>

    <ul class="contact-list">
      <li class="contact-item">
        <svg class="contact-icon" viewBox="0 0 26 26" aria-hidden="true">
          <path d="M13 3a8 8 0 0 0-8 8c0 6 8 12 8 12s8-6 8-12a8 8 0 0 0-8-8z"/>
          <circle cx="13" cy="11" r="3"/>
        </svg>
        4/15 Brenton rd, Kelmore. 2047
      </li>
      <li class="contact-item">
        <svg class="contact-icon" viewBox="0 0 26 26" aria-hidden="true">
          <rect x="8" y="2" width="11" height="22" rx="2"/>
          <line x1="11" y1="20" x2="16" y2="20"/>
          <rect x="10.5" y="5" width="6" height="6"/>
        </svg>
        00000 00000
      </li>
      <li class="contact-item">
        <svg class="contact-icon" viewBox="0 0 26 26" aria-hidden="true">
          <rect x="2" y="6" width="22" height="15" rx="1"/>
          <path d="M2 7l11 8 11-8"/>
        </svg>
        hello@zelvora-example.com.au
      </li>
      <li class="contact-item">
        <svg class="contact-icon" viewBox="0 0 26 26" aria-hidden="true">
          <circle cx="13" cy="13" r="10"/>
          <ellipse cx="13" cy="13" rx="4.5" ry="10"/>
          <line x1="3" y1="13" x2="23" y2="13"/>
          <path d="M5 7.5h16M5 18.5h16"/>
        </svg>
        www.zelvora-example.com.au
      </li>
    </ul>

    <div class="divider"></div>
    <div class="person-name">Peter Hawkley</div>
    <div class="person-role">Director</div>
  </div>
</body>
</html>
```